Zielgruppe
TECHNIKVERLEIH
EVENTMANAGEMENT
BETRIEBSSICHERHEIT
VERANSTALTUNGSSERVICE
SOLAR
Aufgabenstellung
Texte anhand der 'auftrag_o42unpfuask7_lunoquart.pdf', Teaser Text für die Startseite selbst bestimmen, Farben anhand der Logos im Anhand und Ausgabe für Photoshop, XD oder PDF
Designt werden sollen die Startseite sowie eine Unterseite.

```html
<!DOCTYPE html>
<html lang="de">
<head>
<meta charset="utf-8">
<title>Lunoquart – Solar</title>
<link href="https://fonts.googleapis.com/css2?family=Open+Sans:wght@400;600;700&display=swap" rel="stylesheet">
<style>
:root{
  --white:#ffffff;
  --ink:#111111;
  --text-grey:#555555;
  --section-bg:#d6d6d6;
  --footer-bg:#2b292c;
  --accent:#9b85c0;
  --frame:#333333;
  --hero-a:#3a3a3a;
  --hero-b:#6b6b6b;
  --panel-a:#2c3270;
  --panel-b:#6f78b8;
}
*{margin:0;padding:0;box-sizing:border-box}
html,body{width:837px;height:1200px;overflow:hidden}
body{font-family:"Open Sans",sans-serif;background:var(--white);position:relative}
.site-header{position:absolute;top:0;left:0;width:837px;height:59px;background:var(--white)}
.brand{position:absolute;display:flex;align-items:center;gap:6px;font-weight:600;letter-spacing:.5px}
.brand .mark{width:10px;height:10px}
.brand-header{left:51px;top:20px;font-size:17px;color:var(--ink)}
.brand-header .mark{background:var(--accent)}
.main-nav{position:absolute;right:54px;top:26px;display:flex;gap:16px;font-size:8.5px;font-weight:600;color:var(--ink)}
.main-nav .active{color:var(--accent)}
.hero{position:absolute;top:59px;left:0;width:837px;height:222px;background:linear-gradient(135deg,var(--hero-a),var(--hero-b) 55%,var(--hero-a));display:flex;align-items:center;justify-content:center}
.hero h1{color:var(--white);font-size:35px;font-weight:700;margin-top:-16px}
.content{position:absolute;top:281px;left:0;width:837px;height:612px;background:var(--section-bg)}
.content h2{position:absolute;top:66px;left:0;width:837px;text-align:center;font-size:25.5px;line-height:27px;font-weight:700;color:var(--ink)}
.frame{position:absolute;border:1px solid var(--frame)}
.panel-photo{position:absolute;left:268px;top:192px;width:299px;height:133px;background:linear-gradient(120deg,var(--panel-a),var(--panel-b) 50%,var(--panel-a))}
.copy{position:absolute;left:148px;width:545px;font-size:10px;line-height:16px;color:var(--text-grey)}
.copy strong{color:var(--ink);font-weight:600}
.copy-1{top:400px}
.copy-2{top:514px;left:149px}
.site-footer{position:absolute;top:893px;left:0;width:837px;height:307px;background:var(--footer-bg);color:var(--white)}
.brand-footer{left:0;width:837px;justify-content:center;top:78px;font-size:24px;color:var(--white)}
.brand-footer .mark{width:13px;height:13px;background:var(--white)}
.footer-nav{position:absolute;top:159px;left:0;width:837px;display:flex;justify-content:center;gap:16px;font-size:8.5px;font-weight:600}
.social{position:absolute;top:196px;left:0;width:837px;display:flex;justify-content:center;gap:20px}
.social span{width:10px;height:10px;border-radius:50%;background:var(--white)}
.copyright{position:absolute;top:282px;left:0;width:837px;text-align:center;font-size:8.5px;color:#bbbbbb}
</style>
</head>
<body>
<header class="site-header">
  <div class="brand brand-header"><span class="mark"></span>lunoquart</div>
  <nav class="main-nav">
    <span>TECHNOLOGY RENTAL</span><span>EVENT MANAGEMENT</span><span>OPERATIONAL RELABILITY</span><span>EVENT SERVICE</span><span class="active">SOLAR</span>
  </nav>
</header>
<section class="hero" role="img" aria-label="Hausdach mit Solarmodulen in Graustufen">
  <h1>Solar</h1>
</section>
<main class="content">
  <h2>VERANTWORTUNG ÜBERNEHMEN<br>und die Zukunft mitgestalten -<br>regenerative Energien mitLunoquart-Solar</h2>
  <div class="frame" style="left:314px;top:169px;width:39px;height:205px"></div>
  <div class="frame" style="left:252px;top:219px;width:39px;height:112px"></div>
  <div class="frame" style="left:439px;top:300px;width:39px;height:39px"></div>
  <div class="frame" style="left:497px;top:300px;width:39px;height:57px"></div>
  <div class="panel-photo" role="img" aria-label="Nahaufnahme blauer Solarmodule auf einem Ziegeldach"></div>
  <p class="copy copy-1"><strong>Mit dem Aufbau des neusten</strong> Ressorts der Lunoquart GmbH übernimmt unser Unternehmen echte Verantwortung. Durch die Förderung alternativer Energiesysteme erfüllen wir unsere Pflicht, die Umwelt zu schonen und folgenden Generationen eine lebenswerte Zukunft zu garantieren. Dazu planen und errichten wir Photovoltaikanlagen auf Carports, Garagen, Flach- und Schrägdächern sowie auf Industrieflächen. Dank unseres stetig wachsenden Angebotes an individuellen Lösungen für die Energieversorgung durch selbst produzierten Solarstrom, fördern wir aktiv den Ausbau der erneuerbaren Energien in Deutschland.</p>
  <p class="copy copy-2">Durch die Entwicklung speziell zugeschnittener Konzepte zur Erzeugung nachhaltigen Solarstroms für jeden unserer Kunden möchten wir die Zukunft gemeinsam mit Ihnen aktiv gestalten, statt nur ein Teil von ihr zu sein!</p>
</main>
<footer class="site-footer">
  <div class="brand brand-footer"><span class="mark"></span>lunoquart</div>
  <nav class="footer-nav">
    <span>TECHNOLOGY RENTAL</span><span>EVENT MANAGEMENT</span><span>OPERATIONAL RELABILITY</span><span>EVENT SERVICE</span><span>SOLAR</span>
  </nav>
  <div class="social" aria-label="Soziale Netzwerke"><span></span><span></span><span></span></div>
  <p class="copyright">© Copyright 2022 LunoQuart GmbH. All Rights Reserved</p>
</footer>
</body>
</html>
```